Two (Similar) Posters - Both 11" x 17"

We are looking for two posters - both 11" x 17" (vertical orientation) - to promote two consecutive, cardiology-related events:

Poster #1) The Inaugural New York RMC Quizline Competition, Cocktail Reception and Whiskey Tasting (http://brelvan-hsq.org/quizline-and-reception)

and

Poster #2) The 89th Annual Scientific Session and 27th Annual Meeting (http://brelvan-hsq.org/2017annualmtg)

#1 is a cocktail party with a whiskey tasting that will also feature a gameshow-like event with the med students, and #2 is an educational conference for doctors

Target Market(s)

Healthcare providers (Please do not include stock images of medical professionals; in fact, please use caution with any stock imagery, as it most likely will not be appropriate.)

Industry/Entity Type

Education

Colors

Designer to choose colors to be used in the design.

Requirements
Must have
• Each poster design should include:
• - the 4 logos of the participating organizations (I can upload various other versions if needed) along with the "wording" that goes alongside each one (see "STD_small" image as an example)
• - name of event
• - date, time and location
• - where to register
• - where to get more information
• - some artistic flavor or detailing
• Final (raw) files in an .ai, .psd, .eps or .idml format are required upon project completion.
Nice to have
• It's not crucial that these two posters "match," but it would be nice if they at least coordinated with each other. Would be nice if the designer could stay close to our color scheme (can be found here - http://brelvan-hsq.org/), but this isn't crucial. Posters should be upscale, neat and professional.
Should not have
• Should not be too difficult to read. These are posters that will likely be hanging on a bulletin board in hospital staff break rooms. Should not be too cartoon-like or silly. The two should not look EXACTLY the same in case people think that they are the same poster.

```html
<!DOCTYPE html>
<html lang="en">
<head>
<meta charset="utf-8">
<title>Save the Date – New York RMC Quizline Competition</title>
<link rel="stylesheet" href="https://fonts.googleapis.com/css2?family=Noto+Serif:ital,wght@1,400;1,600&family=Arimo:wght@400;700&display=swap">
<style>
  :root {
    --page-bg: #eceef0;
    --navy: #0e2f6e;
    --navy-deep: #0a2457;
    --gold: #e3a827;
    --gold-light: #f6e38c;
    --gold-pale: #fbf0b4;
    --bronze: #7a3a12;
    --white: #ffffff;
    --ink: #1a2a55;
  }
  html, body {
    margin: 0;
    padding: 0;
    width: 1200px;
    height: 1000px;
    overflow: hidden;
    background: var(--page-bg);
  }
  .poster {
    position: absolute;
    left: 294px;
    top: 30px;
    width: 566px;
    height: 870px;
    transform: scale(1.08);
    transform-origin: 0 0;
    background: radial-gradient(ellipse at 50% 40%, var(--navy) 0%, var(--navy-deep) 100%);
    overflow: hidden;
    box-shadow: 0 6px 18px rgba(0,0,0,.18);
    font-family: "Noto Serif", Georgia, serif;
    font-style: italic;
  }
  .ornament {
    position: absolute;
    background: linear-gradient(135deg, var(--gold-light), var(--gold));
    opacity: .55;
  }
  .ornament--corner-left { left: 8px; top: 8px; width: 150px; height: 110px; clip-path: polygon(0 0, 100% 0, 100% 6%, 10% 14%, 6% 100%, 0 100%); }
  .ornament--corner-right { right: 8px; top: 8px; width: 150px; height: 110px; clip-path: polygon(0 0, 100% 0, 100% 100%, 94% 100%, 90% 14%, 0 6%); }
  .ornament--crest { left: 183px; top: 42px; width: 200px; height: 76px; border-radius: 50% 50% 8px 8px; opacity: .75; }
  .crest-rule {
    position: absolute; left: 173px; top: 120px; width: 220px; height: 2px; background: var(--gold);
  }
  .title {
    position: absolute; left: 0; right: 0; top: 140px; margin: 0;
    text-align: center; color: var(--white); font-size: 35px; font-weight: 400;
    letter-spacing: 1px;
  }
  .event-name, .event-details, .pricing {
    position: absolute; left: 0; right: 0; margin: 0; text-align: center; color: var(--gold);
  }
  .event-name { top: 208px; font-size: 19.5px; line-height: 28px; }
  .event-details { top: 343px; font-size: 21px; line-height: 31px; }
  .pricing { top: 522px; font-size: 19.5px; line-height: 31px; }
  .divider { position: absolute; left: 95px; width: 376px; height: 6px; }
  .divider--upper { top: 322px; }
  .divider--lower { top: 477px; }
  .contact {
    position: absolute; left: 0; right: 0; top: 605px; margin: 0;
    text-align: center; color: var(--white);
    font-family: "Arimo", Arial, sans-serif; font-style: normal;
    font-size: 13.5px; line-height: 20px;
  }
  .contact strong { font-weight: 700; }
  .footer-band { position: absolute; left: 0; bottom: 0; width: 566px; height: 240px; }
  .partners {
    position: absolute; left: 0; right: 0; top: 740px; display: flex; justify-content: space-between;
    padding: 0 42px; box-sizing: border-box;
  }
  .partner { width: 150px; text-align: center; }
  .partner__mark {
    width: 64px; height: 64px; margin: 0 auto 8px; border-radius: 50%;
    background: var(--white); border: 3px solid var(--navy);
    box-sizing: border-box;
  }
  .partner__caption {
    margin: 0; color: var(--ink); font-size: 9.5px; line-height: 12px;
  }
  .partner__name { display: block; }
</style>
</head>
<body>
  <main class="poster">
    <div class="ornament ornament--corner-left" role="img" aria-label="Gold filigree corner ornament"></div>
    <div class="ornament ornament--corner-right" role="img" aria-label="Gold filigree corner ornament"></div>
    <div class="ornament ornament--crest" role="img" aria-label="Gold scrollwork header ornament"></div>
    <div class="crest-rule"></div>

    <h1 class="title">SAVE THE DATE</h1>

    <p class="event-name">The Inaugural New York RMC Quizline<br>Competition, Cocktail Reception &amp;<br>Whiskey Tasting</p>

    <svg class="divider divider--upper" viewBox="0 0 376 6" aria-hidden="true">
      <line x1="0" y1="1" x2="376" y2="1" stroke="#e3a827" stroke-width="1"/>
      <line x1="0" y1="5" x2="376" y2="5" stroke="#e3a827" stroke-width="1"/>
      <line x1="0" y1="0" x2="0" y2="6" stroke="#e3a827" stroke-width="2"/>
      <line x1="376" y1="0" x2="376" y2="6" stroke="#e3a827" stroke-width="2"/>
    </svg>

    <p class="event-details">Wednesday, Dec. 6th, 2017<br>From 6:30 p.m. to 10:30 p.m<br>Oak &amp; Ember, 14 E 41st St,<br>New York, NY 10017</p>

    <svg class="divider divider--lower" viewBox="0 0 376 6" aria-hidden="true">
      <line x1="0" y1="1" x2="376" y2="1" stroke="#e3a827" stroke-width="1"/>
      <line x1="0" y1="5" x2="376" y2="5" stroke="#e3a827" stroke-width="1"/>
      <line x1="0" y1="0" x2="0" y2="6" stroke="#e3a827" stroke-width="2"/>
      <line x1="376" y1="0" x2="376" y2="6" stroke="#e3a827" stroke-width="2"/>
    </svg>

    <p class="pricing">Free for BHSQ/HCHM Members<br>and $30 for nonmembers and guests</p>

    <p class="contact">More Information: For more information or to inquire about<br>becoming an exhibitor, call <strong>(212) 555-0147</strong><br>or email <strong>ask@brelvan-hsq.org</strong></p>

    <svg class="footer-band" viewBox="0 0 566 240" preserveAspectRatio="none" aria-hidden="true">
      <defs>
        <linearGradient id="goldFill" x1="0" y1="0" x2="1" y2="0">
          <stop offset="0" stop-color="#d99a1f"/>
          <stop offset=".45" stop-color="#f6e38c"/>
          <stop offset=".75" stop-color="#fbf0b4"/>
          <stop offset="1" stop-color="#e3b53a"/>
        </linearGradient>
        <linearGradient id="bronzeFill" x1="0" y1="0" x2="1" y2="0">
          <stop offset="0" stop-color="#b8751c"/>
          <stop offset=".5" stop-color="#7a3a12"/>
          <stop offset="1" stop-color="#c9872a"/>
        </linearGradient>
      </defs>
      <path d="M0 30 Q 300 95 566 20 L566 240 L0 240 Z" fill="url(#bronzeFill)"/>
      <path d="M0 42 Q 300 110 566 42 L566 240 L0 240 Z" fill="url(#goldFill)"/>
      <path d="M0 50 Q 300 118 566 54" fill="none" stroke="#fff6c8" stroke-width="1.5" opacity=".8"/>
    </svg>

    <section class="partners">
      <div class="partner">
        <div class="partner__mark"></div>
        <p class="partner__caption">Presented by<span class="partner__name">The Brelvan Heart Society, Inc.</span></p>
      </div>
      <div class="partner">
        <div class="partner__mark"></div>
        <p class="partner__caption">of the<span class="partner__name">Northbridge State Chapter</span><span class="partner__name">Halvern College of Heart Medicine</span></p>
      </div>
      <div class="partner">
        <div class="partner__mark"></div>
        <p class="partner__caption">In Association With<span class="partner__name">Corvale Cardiac Center</span></p>
      </div>
    </section>
  </main>
</body>
</html>
```